Tour agency for FIT and groups need a business card design

We need a business card design for a tour agency company that is based in Perth called" BRISK NO", we aim to provide customise, unique and seamless travel arrangement for FIT and groups. We serve both high profile businessperson, government authorities, business partners, executives and investors. The name card should be more professional looking.
Updates

Project Deadline Extended Reason: Have some changes that needed to make, director will be back to office on Monday, sorry for the inconvenience cause. Added Saturday, May 6, 2017

Target Market(s)

High profile businessperson, government authorities, business partners, executives and investors.

Industry/Entity Type

Tourism

Contact Information for Business Card

Brisk NO
Level 1, 214 Marlowe Avenue, Dunreath NO, 6120
www.briskno.com.au

Font styles to use
Serif

Colors

Designer to choose colors to be used in the design.

Requirements
Must have
• My project must have a company logo
Nice to have
• a more professional and solid yet friendly name card design. We may want to include chinese name in the name card as well. Edge of the card can be filled with gold and we think that transparent name cards are interesting.

```html
<!DOCTYPE html>
<html lang="en">
<head>
<meta charset="utf-8">
<title>Brisk NO — Business Card</title>
<link rel="stylesheet" href="https://fonts.googleapis.com/css2?family=Karla:wght@400;500;700&display=swap">
<style>
  :root {
    --brand-blue: #00addc;
    --card-white: #ffffff;
    --ink: #333333;
    --backdrop: #ecebe8;
    --card-w: 800px;
    --card-h: 490px;
  }
  * { box-sizing: border-box; margin: 0; padding: 0; }
  html, body {
    width: 1200px;
    height: 1200px;
    overflow: hidden;
    background: var(--backdrop);
    font-family: "Karla", Arial, sans-serif;
  }
  .canvas {
    width: 1200px;
    height: 1200px;
    display: flex;
    flex-direction: column;
    align-items: center;
    justify-content: center;
    gap: 70px;
  }
  .card {
    position: relative;
    width: var(--card-w);
    height: var(--card-h);
    box-shadow: 0 6px 18px rgba(0,0,0,0.12);
    overflow: hidden;
  }

  /* Front */
  .card-front { background: var(--brand-blue); }
  .edge-tab {
    position: absolute;
    background: var(--card-white);
  }
  .edge-tab--left  { left: 3.6%; top: 38%; width: 6.4%; height: 25%; }
  .edge-tab--right { left: 90%;  top: 24%; width: 6.2%; height: 25%; }
  .front-wordmark {
    position: absolute;
    inset: 0;
    display: flex;
    align-items: center;
    justify-content: center;
    color: var(--card-white);
    font-weight: 700;
    font-size: 84px;
    letter-spacing: 1px;
  }

  /* Back */
  .card-back { background: var(--card-white); color: var(--ink); }
  .info-band {
    position: absolute;
    top: 34%;
    height: 33%;
    background: var(--brand-blue);
  }
  .info-band--stub { left: 0; width: 4.5%; }
  .info-band--name {
    left: 50%;
    right: 0;
    display: flex;
    flex-direction: column;
    align-items: center;
    justify-content: center;
    color: var(--card-white);
  }
  .person-name { font-size: 33px; font-weight: 500; }
  .person-role { font-size: 20px; margin-top: 6px; }
  .back-wordmark {
    position: absolute;
    left: 4.5%;
    width: 45.5%;
    top: 34%;
    height: 33%;
    display: flex;
    align-items: center;
    justify-content: center;
    color: var(--brand-blue);
    font-weight: 700;
    font-size: 56px;
  }
  .address, .contacts {
    position: absolute;
    left: 50%;
    right: 0;
    text-align: center;
    font-size: 19px;
    line-height: 1.3;
  }
  .address { top: 17%; }
  .contacts { top: 71%; }
  .label { color: var(--brand-blue); font-weight: 700; }
</style>
</head>
<body>
<main class="canvas">
  <section class="card card-front" aria-label="Business card front">
    <div class="edge-tab edge-tab--left"></div>
    <div class="edge-tab edge-tab--right"></div>
    <div class="front-wordmark">Brisk NO</div>
  </section>

  <section class="card card-back" aria-label="Business card back">
    <p class="address">
      <span class="label">A:</span> Level 1, 214 Marlowe Avenue,<br>
      Dunreath NO, 6120
    </p>
    <div class="info-band info-band--stub"></div>
    <div class="back-wordmark">Brisk NO</div>
    <div class="info-band info-band--name">
      <p class="person-name">Leon Marsh</p>
      <p class="person-role">Accountant</p>
    </div>
    <p class="contacts">
      <span class="label">E:</span> tessa@briskno.com.au<br>
      <span class="label">M:</span> 08 64027315<br>
      <span class="label">W:</span> www.briskno.com.au
    </p>
  </section>
</main>
</body>
</html>
```